3 screens for iOS app

I need a settings screen, dashboard and leaderboard screen created for an iPhone fitness app that is nearing completion. I have the template in .psd format that needs to be adhered to for consistency, and there are wireframe sketches (literally pen & paper) that you will translate into .psd files for chopping up and adding into the app. Also I need this by Monday.

Settings Screen:

Using the template psd, I need a basic list similar to the setting screen example attached (no icons needed, just text). The list of settings in order are:
Disclaimer
Edit Profile
Feedback
Help!
Terms of Use
Privacy Policy
Push Notifications (switcher icon on/off)
Chatterbook Posts (switcher icon on/off)
Quipster Posts (switcher icon on/off)
Lumora Viewtube Channel
Log Out

Dashboard:
The dashboard tempalte is attached. This dashboard should be inserted between the Grey banner heading and the Orange 14min standard routine bar. It will shift the graph down. The graph should remain unchanged, all you need to do in sert a cool looking dashboard inbetween the grey and orange bars

Dashboard contents:

Three dials (similar to stepmate, paceboard etc - see attached as an example) that display your progress

Dial 1: Title: Week
Dial should change colour as score approaches goal (ideally from green to orange as per icon example attached but not necessarily if you can make it look better)
Inside the dial it needs to include
Total: 598
Goal: 2,000
Days left: 5

Dial 2: Title: Improvement
Inside the dial it needs to include:
Start: 350
PB: 700
+100% in bold, centered

Dial 3: Title: Belt
Inside the dial needs to include:
Total: 9,834
Goal: 25,000

Leaderboard Screen:

Again using the template, with the grey banner heading at the top and tab bar at the bottom:

The leaderboard should be divided into two sections. The first is for my personal scores (as a user). The second section is for all players scores.

Section 1:
- Light grey background, dark grey text. Column titles can be pressed to filter columns. When pressed title changes colour from grey to orange (bold). If you can highlight two of the column titles orange that will be good

Section 2:
- White background, dark grey text. Column titles can be pressed to filter columns.
- Row height should be quite small to fit a large number of names on the screen.

Column titles: (sorry the wireframe sketch text is tough to read)
Rank / Name / W/outs / Wins / Week / Total / Belt

Rank - numeric values from 1-999
Name - text field
W/outs - number from 1-999
Wins - number 1-999
Week - number 1 - 99,999
Total - number 1- 99,999
Belt - coloured dot (white, black, red, blue, green, yellow)

For more info, refer http://www.lumora-example.co/ and download the old app (iphone only) for an idea what we're after.

Industry/Entity Type

Fitness

Colors
f68e4e

Requirements
Must have
• Use the .psd template provided. We're not looking for a redesign.
• The fonts are:
• LeckerliOne Regular
• LobsterTwo Bold
• MeriendaOne Regular
• MVBoli
• GothamExtraLight
• LobsterTwo
Nice to have
• The best dashboard of all time.
Should not have
• changes to fonts,

```html
<!DOCTYPE html>
<html lang="en">
<head>
<meta charset="utf-8">
<title>Leaderboard Screens</title>
<link rel="stylesheet" href="https://fonts.googleapis.com/css2?family=Montserrat:wght@300;400;500;600&family=Open+Sans:wght@400;600&display=swap">
<style>
  :root {
    --canvas: #f2f2f2;
    --bar-dark: #3b4049;
    --bar-darker: #343840;
    --row-white: #ffffff;
    --row-grey: #efefef;
    --row-alt: #f4f4f4;
    --divider: #dedede;
    --text-dark: #2e3136;
    --text-light: #ffffff;
    --text-muted: #8c9097;
    --accent-gold: #f2b134;
    --accent-orange: #f68e4e;
    --gear-orange: #e8743b;
    --battery: #4cd964;
    --results-green: #9be35a;
  }
  * { box-sizing: border-box; margin: 0; padding: 0; }
  html, body {
    width: 1162px; height: 1200px; overflow: hidden;
    background: var(--canvas);
    font-family: "Open Sans", Arial, sans-serif;
    color: var(--text-dark);
  }
  .stage {
    display: flex; gap: 56px; justify-content: center;
    padding-top: 165px;
  }
  .screen {
    width: 497px; height: 870px; position: relative;
    background: var(--row-white);
    box-shadow: 0 2px 10px rgba(0,0,0,.08);
    display: flex; flex-direction: column;
  }
  .status-bar {
    height: 36px; background: var(--bar-dark); color: var(--text-light);
    display: flex; align-items: center; justify-content: space-between;
    padding: 0 10px; font-family: "Montserrat", sans-serif; font-weight: 500; font-size: 19px;
  }
  .signal { display: flex; align-items: center; gap: 3px; width: 110px; }
  .signal i { width: 8px; height: 8px; border-radius: 50%; background: var(--text-light); display: block; }
  .battery { width: 110px; display: flex; justify-content: flex-end; }
  .battery span {
    width: 36px; height: 14px; border: 1.5px solid var(--text-light); border-radius: 3px; padding: 1px;
    display: block; position: relative;
  }
  .battery span::before { content: ""; display: block; height: 100%; background: var(--battery); border-radius: 1px; }
  .battery span::after { content: ""; position: absolute; right: -4px; top: 3px; width: 2px; height: 5px; background: var(--text-light); }
  .nav-bar {
    height: 62px; background: var(--bar-dark); color: var(--text-light);
    display: flex; align-items: center; justify-content: center; position: relative;
  }
  .nav-title { font-family: "Montserrat", sans-serif; font-weight: 300; font-size: 29px; }
  .settings-icon { position: absolute; left: 10px; top: 14px; width: 34px; height: 34px; }
  .table-row {
    display: grid;
    grid-template-columns: 54px 120px 42px 72px 84px 70px 55px;
    align-items: center; text-align: center;
    font-size: 14px;
  }
  .table-row .name { text-align: left; padding-left: 8px; font-family: "Montserrat", sans-serif; font-weight: 600; font-size: 13.5px; }
  .table-row .wins { text-align: right; padding-right: 8px; }
  .column-head {
    height: 32px; background: var(--bar-dark); color: var(--text-light);
    font-family: "Montserrat", sans-serif; font-size: 14px;
  }
  .column-head .name { font-weight: 400; font-size: 14px; text-align: center; padding-left: 0; }
  .column-head .wins { text-align: center; padding-right: 0; }
  .column-head .active { color: var(--accent-gold); }
  .my-score { height: 60px; background: var(--row-grey); }
  .players { flex: 1; overflow: hidden; }
  .players .table-row { height: 47.5px; border-bottom: 1px solid var(--divider); background: var(--row-white); }
  .screen--striped .players .table-row { border-bottom: none; }
  .screen--striped .players .table-row:nth-child(even) { background: var(--row-alt); }
  .tab-bar {
    height: 78px; background: var(--bar-dark); position: relative;
    display: grid; grid-template-columns: 1fr 1fr 1.3fr 1fr 1fr;
    font-family: "Montserrat", sans-serif; font-size: 15px; color: var(--text-muted);
  }
  .tab { display: flex; flex-direction: column; align-items: center; justify-content: flex-end; padding-bottom: 6px; gap: 2px; position: relative; }
  .tab svg { width: 40px; height: 40px; }
  .tab--active { color: var(--text-light); }
  .tab--start { z-index: 1; }
  .start-button {
    position: absolute; top: -20px; left: 50%; transform: translateX(-50%);
    width: 118px; height: 118px; border-radius: 50%;
    background: var(--bar-darker); border: 2px solid #4a505a;
  }
  .start-button svg { position: absolute; left: 40px; top: 18px; width: 40px; height: 44px; }
  .tab--start .label { position: relative; }
</style>
</head>
<body>
<main class="stage">
  <!-- Plain variant -->
  <section class="screen">
    <div class="status-bar">
      <div class="signal"><i></i><i></i><i></i><i></i><i></i>
        <svg width="18" height="14" viewBox="0 0 18 14"><path d="M1 5a11 11 0 0 1 16 0M4 8a7 7 0 0 1 10 0M7 11a3 3 0 0 1 4 0" stroke="#fff" stroke-width="2" fill="none"/></svg></div>
      <span>9:00 AM</span>
      <div class="battery"><span></span></div>
    </div>
    <header class="nav-bar">
      <svg class="settings-icon" viewBox="0 0 24 24" fill="none" stroke="var(--gear-orange)" stroke-width="1.8"><circle cx="12" cy="12" r="3.2"/><path d="M12 2.5l1.6 2.6 3-.8.8 3 2.6 1.6-1.3 2.6 1.3 2.7-2.6 1.6-.8 3-3-.8L12 21.5l-1.6-2.6-3 .8-.8-3-2.6-1.6L5.3 12 4 9.3l2.6-1.6.8-3 3 .8z"/></svg>
      <h1 class="nav-title">Leaderboard</h1>
    </header>
    <div class="table-row column-head"><span>Rank</span><span class="name">Name</span><span>W/out</span><span class="wins active">Wins</span><span>Week</span><span class="active">Total</span><span>Belt</span></div>
    <div class="table-row my-score"><span>01</span><span class="name">Marla Quinton</span><span>10</span><span class="wins">6</span><span>1,271</span><span>9,810</span><span>0</span></div>
    <div class="table-row column-head"><span>Rank</span><span class="name">Name</span><span>W/out</span><span class="wins active">Wins</span><span>Week</span><span class="active">Total</span><span>Belt</span></div>
    <div class="players">
      <div class="table-row"><span>02</span><span class="name">Toby Larkwell</span><span>24</span><span class="wins">27</span><span>1,978</span><span>10,111</span><span>0</span></div>
      <div class="table-row"><span>03</span><span class="name">Jonas Perrow</span><span>29</span><span class="wins">14</span><span>1,678</span><span>9,812</span><span>0</span></div>
      <div class="table-row"><span>04</span><span class="name">Ravi Okonde</span><span>10</span><span class="wins">6</span><span>1,271</span><span>9,810</span><span>0</span></div>
      <div class="table-row"><span>02</span><span class="name">Toby Larkwell</span><span>24</span><span class="wins">27</span><span>1,978</span><span>10,111</span><span>0</span></div>
      <div class="table-row"><span>03</span><span class="name">Jonas Perrow</span><span>29</span><span class="wins">14</span><span>1,678</span><span>9,812</span><span>0</span></div>
      <div class="table-row"><span>04</span><span class="name">Ravi Okonde</span><span>10</span><span class="wins">6</span><span>1,271</span><span>9,810</span><span>0</span></div>
      <div class="table-row"><span>02</span><span class="name">Toby Larkwell</span><span>24</span><span class="wins">27</span><span>1,978</span><span>10,111</span><span>0</span></div>
      <div class="table-row"><span>03</span><span class="name">Jonas Perrow</span><span>29</span><span class="wins">14</span><span>1,678</span><span>9,812</span><span>0</span></div>
      <div class="table-row"><span>04</span><span class="name">Ravi Okonde</span><span>10</span><span class="wins">6</span><span>1,271</span><span>9,810</span><span>0</span></div>
      <div class="table-row"><span>02</span><span class="name">Toby Larkwell</span><span>24</span><span class="wins">27</span><span>1,978</span><span>10,111</span><span>0</span></div>
      <div class="table-row"><span>03</span><span class="name">Jonas Perrow</span><span>29</span><span class="wins">14</span><span>1,678</span><span>9,812</span><span>0</span></div>
      <div class="table-row"><span>04</span><span class="name">Ravi Okonde</span><span>10</span><span class="wins">6</span><span>1,271</span><span>9,810</span><span>0</span></div>
    </div>
    <nav class="tab-bar">
      <div class="tab"><svg viewBox="0 0 40 40" fill="none" stroke="#8c9097" stroke-width="1.8"><circle cx="20" cy="13" r="7"/><path d="M6 37v-5c0-6 6-9 14-9s14 3 14 9v5z"/></svg><span class="label">Profile</span></div>
      <div class="tab tab--active"><svg viewBox="0 0 40 40" fill="none" stroke="var(--results-green)" stroke-width="2"><path d="M3 33l9-10 5 6 8-11 4 4 8-11"/><path d="M3 29l9-10 5 6 8-11 4 4 8-11" opacity=".6"/></svg><span class="label">Results</span></div>
      <div class="tab tab--start"><div class="start-button"><svg viewBox="0 0 40 44"><path d="M4 2l34 20L4 42z" fill="#8c9097"/></svg></div><span class="label">Start</span></div>
      <div class="tab"><svg viewBox="0 0 40 40"><path d="M12 24l-5 13 6-3 3 5 4-10M28 24l5 13-6-3-3 5-4-10" fill="none" stroke="#8c9097" stroke-width="1.8"/><circle cx="20" cy="15" r="11" fill="var(--gear-orange)"/><text x="20" y="20" text-anchor="middle" font-family="Montserrat, sans-serif" font-size="14" font-weight="600" fill="#fff">2</text></svg><span class="label">Challenges</span></div>
      <div class="tab"><svg viewBox="0 0 40 40" fill="none" stroke="#8c9097" stroke-width="1.8"><path d="M4 36c2-12 6-22 12-28 3-3 7-3 8 0l-2 5-5 1-2 8c3-3 9-4 13-1 5 3 7 9 6 15z"/></svg><span class="label">Routines</span></div>
    </nav>
  </section>

  <!-- Striped variant -->
  <section class="screen screen--striped">
    <div class="status-bar">
      <div class="signal"><i></i><i></i><i></i><i></i><i></i>
        <svg width="18" height="14" viewBox="0 0 18 14"><path d="M1 5a11 11 0 0 1 16 0M4 8a7 7 0 0 1 10 0M7 11a3 3 0 0 1 4 0" stroke="#fff" stroke-width="2" fill="none"/></svg></div>
      <span>9:00 AM</span>
      <div class="battery"><span></span></div>
    </div>
    <header class="nav-bar">
      <svg class="settings-icon" viewBox="0 0 24 24" fill="none" stroke="var(--gear-orange)" stroke-width="1.8"><circle cx="12" cy="12" r="3.2"/><path d="M12 2.5l1.6 2.6 3-.8.8 3 2.6 1.6-1.3 2.6 1.3 2.7-2.6 1.6-.8 3-3-.8L12 21.5l-1.6-2.6-3 .8-.8-3-2.6-1.6L5.3 12 4 9.3l2.6-1.6.8-3 3 .8z"/></svg>
      <h1 class="nav-title">Leaderboard</h1>
    </header>
    <div class="table-row column-head"><span>Rank</span><span class="name">Name</span><span>W/out</span><span class="wins active">Wins</span><span>Week</span><span class="active">Total</span><span>Belt</span></div>
    <div class="table-row my-score"><span>01</span><span class="name">Marla Quinton</span><span>10</span><span class="wins">6</span><span>1,271</span><span>9,810</span><span>0</span></div>
    <div class="table-row column-head"><span>Rank</span><span class="name">Name</span><span>W/out</span><span class="wins active">Wins</span><span>Week</span><span class="active">Total</span><span>Belt</span></div>
    <div class="players">
      <div class="table-row"><span>02</span><span class="name">Toby Larkwell</span><span>24</span><span class="wins">27</span><span>1,978</span><span>10,111</span><span>0</span></div>
      <div class="table-row"><span>03</span><span class="name">Jonas Perrow</span><span>29</span><span class="wins">14</span><span>1,678</span><span>9,812</span><span>0</span></div>
      <div class="table-row"><span>04</span><span class="name">Ravi Okonde</span><span>10</span><span class="wins">6</span><span>1,271</span><span>9,810</span><span>0</span></div>
      <div class="table-row"><span>02</span><span class="name">Toby Larkwell</span><span>24</span><span class="wins">27</span><span>1,978</span><span>10,111</span><span>0</span></div>
      <div class="table-row"><span>03</span><span class="name">Jonas Perrow</span><span>29</span><span class="wins">14</span><span>1,678</span><span>9,812</span><span>0</span></div>
      <div class="table-row"><span>04</span><span class="name">Ravi Okonde</span><span>10</span><span class="wins">6</span><span>1,271</span><span>9,810</span><span>0</span></div>
      <div class="table-row"><span>02</span><span class="name">Toby Larkwell</span><span>24</span><span class="wins">27</span><span>1,978</span><span>10,111</span><span>0</span></div>
      <div class="table-row"><span>03</span><span class="name">Jonas Perrow</span><span>29</span><span class="wins">14</span><span>1,678</span><span>9,812</span><span>0</span></div>
      <div class="table-row"><span>04</span><span class="name">Ravi Okonde</span><span>10</span><span class="wins">6</span><span>1,271</span><span>9,810</span><span>0</span></div>
      <div class="table-row"><span>02</span><span class="name">Toby Larkwell</span><span>24</span><span class="wins">27</span><span>1,978</span><span>10,111</span><span>0</span></div>
      <div class="table-row"><span>03</span><span class="name">Jonas Perrow</span><span>29</span><span class="wins">14</span><span>1,678</span><span>9,812</span><span>0</span></div>
      <div class="table-row"><span>04</span><span class="name">Ravi Okonde</span><span>10</span><span class="wins">6</span><span>1,271</span><span>9,810</span><span>0</span></div>
    </div>
    <nav class="tab-bar">
      <div class="tab"><svg viewBox="0 0 40 40" fill="none" stroke="#8c9097" stroke-width="1.8"><circle cx="20" cy="13" r="7"/><path d="M6 37v-5c0-6 6-9 14-9s14 3 14 9v5z"/></svg><span class="label">Profile</span></div>
      <div class="tab tab--active"><svg viewBox="0 0 40 40" fill="none" stroke="var(--results-green)" stroke-width="2"><path d="M3 33l9-10 5 6 8-11 4 4 8-11"/><path d="M3 29l9-10 5 6 8-11 4 4 8-11" opacity=".6"/></svg><span class="label">Results</span></div>
      <div class="tab tab--start"><div class="start-button"><svg viewBox="0 0 40 44"><path d="M4 2l34 20L4 42z" fill="#8c9097"/></svg></div><span class="label">Start</span></div>
      <div class="tab"><svg viewBox="0 0 40 40"><path d="M12 24l-5 13 6-3 3 5 4-10M28 24l5 13-6-3-3 5-4-10" fill="none" stroke="#8c9097" stroke-width="1.8"/><circle cx="20" cy="15" r="11" fill="var(--gear-orange)"/><text x="20" y="20" text-anchor="middle" font-family="Montserrat, sans-serif" font-size="14" font-weight="600" fill="#fff">2</text></svg><span class="label">Challenges</span></div>
      <div class="tab"><svg viewBox="0 0 40 40" fill="none" stroke="#8c9097" stroke-width="1.8"><path d="M4 36c2-12 6-22 12-28 3-3 7-3 8 0l-2 5-5 1-2 8c3-3 9-4 13-1 5 3 7 9 6 15z"/></svg><span class="label">Routines</span></div>
    </nav>
  </section>
</main>
</body>
</html>
```